Design & Build a WordPress Website for “Quietfern Meditation” (Australian Charity Rebrand)

We are a registered Australian charity currently known as Tavolin Meditation Australia.

We are rebranding our public identity to “Quietfern Meditation” to make the meditation practice easier to understand and more relatable for people in Australia and New Zealand.

We are looking for an experienced WordPress designer + developer to design and build a complete website that reflects:

Peace

Trust

Authentic Himalayan roots

Simplicity

Spiritual depth without being religious

Warmth, friendliness, and community feeling

This is not a corporate website. This is a meditation movement website for a non-profit organisation.

Target Market(s)

Australia and New Zealand - Age 25-65

Industry/Entity Type

Not of profit meditation organisation

Requirements
Must have
• Included in the design brief attached
Nice to have
Should not have

```html
<!DOCTYPE html>
<html lang="en">
<head>
<meta charset="utf-8">
<title>Quietfern Meditation – Home</title>
<link href="https://fonts.googleapis.com/css2?family=Gloock&family=Rozha+One&family=Roboto:wght@400;500;700&display=swap" rel="stylesheet">
<style>
:root{
  --green:#5b7a45;
  --green-deep:#4a6a38;
  --footer:#5f7e4b;
  --gold:#9b8450;
  --mist:#f2f8f9;
  --ink:#2f2f2f;
  --muted:#555;
  --white:#fff;
}
*{margin:0;padding:0;box-sizing:border-box}
html,body{width:1200px;height:1200px;overflow:hidden;background:var(--white);font-family:"Roboto",Arial,sans-serif;color:var(--ink)}
.page{position:absolute;top:0;width:419px;height:1200px;overflow:hidden}
.page--home{left:137px}
.page--lower{left:661px}
.abs{position:absolute}
.band{position:absolute;left:0;width:419px}
.heading{font-family:"Gloock",Georgia,serif;color:var(--green-deep);font-weight:400;line-height:1.15}
.btn{position:absolute;height:11px;background:var(--gold);color:var(--white);font-size:4.2px;font-weight:500;display:flex;align-items:center;justify-content:center;gap:2px;border-radius:1px}
.btn::after{content:"";width:3px;height:3px;border:0.6px solid var(--white);border-radius:50%}
.copy{font-size:4.4px;line-height:1.6;color:var(--ink);text-align:justify}
.photo{position:absolute}

/* header */
.topbar{top:0;height:23px;background:var(--white)}
.brand{left:18px;top:8px;font-family:"Gloock",Georgia,serif;font-size:8px;color:var(--green-deep);letter-spacing:.1px}
.contact-line{top:8px;font-size:5px;color:var(--ink);display:flex;align-items:center;gap:3px}
.mainnav{top:23px;height:15px;background:var(--green);display:flex;align-items:center}
.mainnav span{position:absolute;font-family:"Gloock",Georgia,serif;font-size:4.6px;color:var(--white)}
.mainnav i{position:absolute;top:2px;height:11px;border-left:0.6px dotted rgba(255,255,255,.7)}

/* hero */
.hero{top:38px;height:296px;background:linear-gradient(170deg,#aac3dd 0%,#d9e3ea 22%,#6f8796 45%,#3f5a4a 70%,#5d4c3c 100%)}
.hero-title{left:35px;top:77px;font-family:"Rozha One",Georgia,serif;font-size:24px;line-height:28px;color:var(--white)}
.hero .copy{left:35px;top:165px;width:157px;color:var(--white)}
.arrow{position:absolute;top:140px;width:18px;height:18px;background:var(--gold);display:flex;align-items:center;justify-content:center}
.dots{top:334px;height:9px;background:#e9edf0;display:flex;justify-content:center;align-items:center;gap:4px}
.dots b{width:5px;height:5px;border-radius:50%;background:#cfcfcf}
.dots b:first-child{background:var(--gold)}

/* left sections */
.about-what{top:343px;height:242px;background:linear-gradient(180deg,#e5e9ef,#dfe6ee 50%,#eef1f4)}
.about-org{top:585px;height:175px;background:var(--mist)}
.sessions{top:760px;height:193px;background:linear-gradient(100deg,#3b2f24 0%,#5a4430 40%,#9a7252 70%,#4d3b2e 100%)}
.volunteer{height:178px;background:linear-gradient(180deg,#e7e9ea,#eeeeee 60%,#f2f2f2)}
.events-peek{top:1131px;height:69px;background:var(--mist)}
.list{font-size:4.4px;line-height:1.6;list-style:none}
.list li::before{content:"● ";font-size:3.5px}

/* right column */
.events{top:242px;height:280px;background:var(--mist)}
.events-intro{left:15px;top:24px;width:129px;height:233px;border-radius:5px;background:linear-gradient(180deg,#a9b8e8 0%,#c7c4e0 35%,#e8c3a6 55%,#5f8a4f 72%,#3f5e38 100%)}
.events-intro .heading{position:absolute;left:0;right:0;top:15px;text-align:center;font-size:11px;line-height:13px}
.event-card{position:absolute;width:80px;height:106px;background:var(--white);box-shadow:0 0 2px rgba(0,0,0,.25)}
.event-card .pic{position:absolute;left:3px;top:3px;width:74px;height:48px}
.event-card p{position:absolute;left:0;right:0;text-align:center;font-size:4.6px;color:#444}
.event-card p.name{font-weight:700}
.resources{top:522px;height:274px;background:linear-gradient(180deg,#e3e3e3,#ececec 50%,#e6e6e6)}
.article{position:absolute;top:45px;width:92px;height:202px;background:rgba(240,240,240,.85);box-shadow:0 0 2px rgba(0,0,0,.25)}
.article .pic{position:absolute;left:3px;top:3px;width:86px;height:128px}
.article .t{position:absolute;left:4px;font-size:4.6px;color:#555}
.contact{top:796px;height:239px;background:var(--mist)}
.field-label{position:absolute;left:156px;font-size:4.6px;color:#333}
.field{position:absolute;left:156px;width:236px;height:11px;background:var(--white);border:0.6px solid #bbb;border-radius:1px;font-size:3.8px;color:#aaa;padding:3px 4px}
.footer{top:1035px;height:165px;background:var(--footer);color:var(--white)}
.footer h4{position:absolute;font-family:"Gloock",Georgia,serif;font-weight:400;font-size:4.2px;letter-spacing:.2px}
.footer-links{position:absolute;left:184px;top:1076px;list-style:none;font-size:4.4px}
.footer-links li{height:10.5px;display:flex;align-items:center;gap:3px}
.footer-links li::before{content:"→";font-size:4.6px}
.social{position:absolute;top:1108px;width:7px;height:7px;border-radius:50%;background:var(--white)}
</style>
</head>
<body>

<!-- Home page: upper part -->
<section class="page page--home">
  <header class="band topbar">
    <div class="abs brand">QUIETFERN MEDITATION</div>
    <div class="abs contact-line" style="left:251px">
      <svg width="6" height="5" viewBox="0 0 6 5"><rect x="0.3" y="0.3" width="5.4" height="4.4" fill="#777"/><path d="M0.3 0.5 3 2.6 5.7 0.5" stroke="#fff" stroke-width="0.5" fill="none"/></svg>
      hello@quietfern.org
    </div>
    <div class="abs contact-line" style="left:312px">
      <svg width="6" height="6" viewBox="0 0 6 6"><path d="M1 0.5 2.2 0.3 2.8 1.9 2 2.6Q2.8 4 3.8 4.5L4.4 3.7 5.8 4.3 5.6 5.5Q2.5 5.6 0.5 1.8Z" fill="#777"/></svg>
      +61 400 123 456
    </div>
    <div class="btn" style="left:367px;top:7px;width:34px;height:11px;font-size:4.2px">Donate</div>
  </header>

  <nav class="band mainnav">
    <span style="left:22px">Home</span><i style="left:44px"></i>
    <span style="left:53px">About Us</span><i style="left:82px"></i>
    <span style="left:91px">Meditation Sessions</span><i style="left:152px"></i>
    <span style="left:160px">Events &amp; Programs</span><i style="left:220px"></i>
    <span style="left:228px">Project</span><i style="left:254px"></i>
    <span style="left:261px">Resources</span><i style="left:297px"></i>
    <span style="left:305px">Volunteer With Us</span><i style="left:361px"></i>
    <span style="left:368px">Contact Us</span>
  </nav>

  <section class="band hero" role="img" aria-label="Woman meditating on a wooden deck facing snowy Himalayan peaks">
    <h1 class="abs hero-title">Welcome To<br>Quietfern<br>Meditation</h1>
    <p class="abs copy">Lorem ipsum dolor sit amet, consectetur adipiscing elit, sed do eiusmod tempor incididunt ut labore et dolore magna aliqua. Vulputate dignissim suspendisse in est ante. Faucibus turpis in eu mi bibendum neque. Sodales ut etiam sit amet nisl purus. Velit laoreet id donec ultrices tincidunt.</p>
    <div class="btn" style="left:35px;top:211px;width:58px">CONTACT US NOW</div>
    <div class="arrow" style="left:0"><svg width="5" height="7" viewBox="0 0 5 7"><path d="M4 0.5 1 3.5 4 6.5" stroke="#fff" fill="none" stroke-width="1"/></svg></div>
    <div class="arrow" style="right:0"><svg width="5" height="7" viewBox="0 0 5 7"><path d="M1 0.5 4 3.5 1 6.5" stroke="#fff" fill="none" stroke-width="1"/></svg></div>
  </section>
  <div class="band dots"><b></b><b></b><b></b><b></b></div>

  <section class="band about-what" role="img" aria-label="Misty mountain backdrop">
    <h2 class="abs heading" style="left:18px;top:85px;font-size:11px">What Is Quietfern Meditation</h2>
    <p class="abs copy" style="left:18px;top:99px;width:190px">Quietfern Meditation is a simple, natural meditation technique taught freely to help people experience inner peace, clarity, and emotional balance. We conduct:</p>
    <ul class="abs list" style="left:18px;top:113px">
      <li>Free meditation sessions</li>
      <li>Community programs</li>
      <li>Events (International Yoga Day, group meditations, etc.)</li>
      <li>Donation drives for building a meditation centre (community centre project)</li>
    </ul>
    <div class="btn" style="left:18px;top:152px;width:43px">Know More</div>
    <div class="photo" role="img" aria-label="Woman seated cross-legged in meditation" style="left:250px;top:48px;width:114px;height:155px;background:linear-gradient(180deg,#d8c2ad 0%,#c9a98c 40%,#2b2b2e 70%,#353539 100%);border-radius:50px 50px 30px 30px;opacity:.9"></div>
  </section>

  <section class="band about-org">
    <div class="photo" role="img" aria-label="Woman meditating on a hillside above a valley" style="left:31px;top:27px;width:162px;height:121px;border-radius:0 60px 0 60px;background:linear-gradient(180deg,#9bb6cf 0%,#c9d6de 35%,#4f6b4a 60%,#6b7d45 100%)"></div>
    <h2 class="abs heading" style="left:213px;top:48px;font-size:11px;line-height:13px">About The Organisation :<br>Tavolin Meditation Australia</h2>
    <p class="abs copy" style="left:213px;top:78px;width:189px">Welcome to Tavolin Meditation Australia – your bright, bubbly oasis of calm in the vast digital desert. Kick off your shoes, find your favourite comfy spot, and prepare to embark on a life-changing journey to improved health, wellness, and spiritual awakening, all served with a sprinkle of playfulness and a dash of joy.</p>
    <div class="btn" style="left:213px;top:117px;width:43px">Know More</div>
  </section>

  <section class="band sessions" role="img" aria-label="Woman meditating on a rock at sunset">
    <h2 class="abs heading" style="left:18px;top:62px;font-size:11px;color:var(--white)">Check Our Meditation Sessions</h2>
    <p class="abs copy" style="left:18px;top:76px;width:240px;color:var(--white)">Lorem ipsum dolor sit amet, consectetur adipiscing elit, sed do eiusmod tempor incididunt ut labore et dolore magna aliqua. Tempor orci eu lobortis elementum nibh tellus molestie. Sagittis orci a scelerisque purus semper eget duis at. Commodo odio aenean sed adipiscing diam donec. Faucibus scelerisque eleifend donec pretium vulputate sapien.</p>
    <div class="btn" style="left:18px;top:114px;width:43px">Know More</div>
  </section>

  <section class="band volunteer" style="top:953px" role="img" aria-label="Faded snowy mountain backdrop">
    <div class="photo" role="img" aria-label="Group of volunteers in tree pose" style="left:47px;top:37px;width:131px;height:94px;background:linear-gradient(90deg,#8c8f9a,#3d4a66 50%,#7a7f8c);border-radius:8px;opacity:.55"></div>
    <h2 class="abs heading" style="left:213px;top:59px;font-size:11px">Volunteer With Us</h2>
    <p class="abs copy" style="left:213px;top:75px;width:189px">Lorem ipsum dolor sit amet, consectetur adipiscing elit, sed do eiusmod tempor incididunt ut labore et dolore magna aliqua. Vulputate dignissim suspendisse in est ante. Faucibus turpis in eu mi bibendum neque. Sodales ut etiam sit amet nisl purus. Velit laoreet id donec ultrices tincidunt.</p>
    <div class="btn" style="left:213px;top:113px;width:43px">Know More</div>
  </section>

  <section class="band events-peek">
    <div class="abs" style="left:15px;top:24px;width:130px;height:60px;border-radius:5px 5px 0 0;background:linear-gradient(180deg,#a9b8e8,#c4c4e2)">
      <div class="heading" style="text-align:center;margin-top:14px;font-size:11px;line-height:13px">Events<br>&amp;<br>Programs</div>
    </div>
    <div class="abs" style="left:153px;top:31px;width:77px;height:50px;background:var(--white);box-shadow:0 0 2px rgba(0,0,0,.25)"><div role="img" aria-label="Indoor yoga class" style="margin:3px;height:44px;background:linear-gradient(180deg,#7a5c6a,#3b3340)"></div></div>
    <div class="abs" style="left:238px;top:31px;width:77px;height:50px;background:var(--white);box-shadow:0 0 2px rgba(0,0,0,.25)"><div role="img" aria-label="Seaside group session" style="margin:3px;height:44px;background:linear-gradient(180deg,#d7dde6,#6b7d94)"></div></div>
    <div class="abs" style="left:322px;top:31px;width:77px;height:50px;background:var(--white);box-shadow:0 0 2px rgba(0,0,0,.25)"><div role="img" aria-label="Outdoor meditation on grass" style="margin:3px;height:44px;background:linear-gradient(180deg,#7c9a5b,#4e6e39)"></div></div>
  </section>
</section>

<!-- Home page: lower part -->
<section class="page page--lower">
  <div class="band" role="img" aria-label="Meditator silhouetted at dusk" style="top:0;height:63px;background:linear-gradient(90deg,#2c2520,#6b4a3a 60%,#3a2a24)"></div>

  <section class="band volunteer" style="top:63px" role="img" aria-label="Faded snowy mountain backdrop">
    <div class="photo" role="img" aria-label="Group of volunteers in tree pose" style="left:47px;top:39px;width:130px;height:97px;background:linear-gradient(90deg,#8c8f9a,#3d4a66 50%,#7a7f8c);border-radius:8px;opacity:.55"></div>
    <h2 class="abs heading" style="left:212px;top:55px;font-size:11px">Volunteer With Us</h2>
    <p class="abs copy" style="left:212px;top:72px;width:189px">Lorem ipsum dolor sit amet, consectetur adipiscing elit, sed do eiusmod tempor incididunt ut labore et dolore magna aliqua. Vulputate dignissim suspendisse in est ante. Faucibus turpis in eu mi bibendum neque. Sodales ut etiam sit amet nisl purus. Velit laoreet id donec ultrices tincidunt.</p>
    <div class="btn" style="left:212px;top:113px;width:43px">Know More</div>
  </section>

  <section class="band events">
    <div class="abs events-intro" role="img" aria-label="Large outdoor group yoga session under trees">
      <h2 class="heading">Events<br>&amp;<br>Programs</h2>
      <div class="btn" style="left:43px;top:59px;width:43px">Check Here</div>
    </div>

    <div class="event-card" style="left:150px;top:31px"><div class="pic" role="img" aria-label="Indoor yoga class" style="background:linear-gradient(180deg,#8a5d6c,#3a3340)"></div><p class="name" style="top:56px">Events Name Here</p><p style="top:67px">Time: 09:30 AM</p><p style="top:78px">Place: Address Will Be Here</p><div class="btn" style="left:19px;top:91px;width:43px">Know More</div></div>
    <div class="event-card" style="left:234px;top:31px"><div class="pic" role="img" aria-label="Seaside group session" style="background:linear-gradient(180deg,#d6dde7,#6c7e95)"></div><p class="name" style="top:56px">Events Name Here</p><p style="top:67px">Time: 09:30 AM</p><p style="top:78px">Place: Address Will Be Here</p><div class="btn" style="left:19px;top:91px;width:43px">Know More</div></div>
    <div class="event-card" style="left:319px;top:31px"><div class="pic" role="img" aria-label="Outdoor meditation on grass" style="background:linear-gradient(180deg,#86a262,#4e6e39)"></div><p class="name" style="top:56px">Events Name Here</p><p style="top:67px">Time: 09:30 AM</p><p style="top:78px">Place: Address Will Be Here</p><div class="btn" style="left:19px;top:91px;width:43px">Know More</div></div>

    <div class="event-card" style="left:150px;top:143px"><div class="pic" role="img" aria-label="Studio class stretching" style="background:linear-gradient(180deg,#eef0f2,#8d8f97)"></div><p class="name" style="top:56px">Events Name Here</p><p style="top:67px">Time: 09:30 AM</p><p style="top:78px">Place: Address Will Be Here</p><div class="btn" style="left:19px;top:91px;width:43px">Know More</div></div>
    <div class="event-card" style="left:234px;top:143px"><div class="pic" role="img" aria-label="Seated group meditation indoors" style="background:linear-gradient(180deg,#b6b0a4,#6f6a62)"></div><p class="name" style="top:56px">Events Name Here</p><p style="top:67px">Time: 09:30 AM</p><p style="top:78px">Place: Address Will Be Here</p><div class="btn" style="left:19px;top:91px;width:43px">Know More</div></div>
    <div class="event-card" style="left:319px;top:143px"><div class="pic" role="img" aria-label="Rooftop group session by the sea" style="background:linear-gradient(180deg,#c9d4e3,#7c8ba0)"></div><p class="name" style="top:56px">Events Name Here</p><p style="top:67px">Time: 09:30 AM</p><p style="top:78px">Place: Address Will Be Here</p><div class="btn" style="left:19px;top:91px;width:43px">Know More</div></div>
  </section>

  <section class="band resources">
    <h2 class="abs heading" style="left:0;right:0;top:24px;text-align:center;font-size:11px">Check Our Helpful Resources</h2>
    <article class="article" style="left:17px"><div class="pic" role="img" aria-label="Women in a meditation class" style="background:linear-gradient(180deg,#b59f8a,#4a5575)"></div><p class="t" style="top:137px;font-weight:500">Article Name Here</p><p class="t" style="top:148px">By: Admin</p><p class="t" style="top:159px;right:4px;line-height:1.1">Lorem ipsum dolor sit amet, consectetur adipiscing elit, sed do eiusmod tempor incididunt ut labore et dolore magna aliqua.</p><p class="t" style="top:188px;left:10px;color:var(--gold)">Read More ⊕</p></article>
    <article class="article" style="left:115px"><div class="pic" role="img" aria-label="Yoga on blue mats in a studio" style="background:linear-gradient(180deg,#a86a4c,#b28a5a 50%,#3f6fc8)"></div><p class="t" style="top:137px;font-weight:500">Article Name Here</p><p class="t" style="top:148px">By: Admin</p><p class="t" style="top:159px;right:4px;line-height:1.1">Lorem ipsum dolor sit amet, consectetur adipiscing elit, sed do eiusmod tempor incididunt ut labore et dolore magna aliqua.</p><p class="t" style="top:188px;left:10px;color:var(--gold)">Read More ⊕</p></article>
    <article class="article" style="left:212px"><div class="pic" role="img" aria-label="Meditation on rocks by a lake" style="background:linear-gradient(180deg,#bcd0e6,#8aa4bf 50%,#7c6e62)"></div><p class="t" style="top:137px;font-weight:500">Article Name Here</p><p class="t" style="top:148px">By: Admin</p><p class="t" style="top:159px;right:4px;line-height:1.1">Lorem ipsum dolor sit amet, consectetur adipiscing elit, sed do eiusmod tempor incididunt ut labore et dolore magna aliqua.</p><p class="t" style="top:188px;left:10px;color:var(--gold)">Read More ⊕</p></article>
    <article class="article" style="left:310px"><div class="pic" role="img" aria-label="Women balancing in tree pose" style="background:linear-gradient(180deg,#d9d3cc,#b4a8a0 55%,#3a74c4)"></div><p class="t" style="top:137px;font-weight:500">Article Name Here</p><p class="t" style="top:148px">By: Admin</p><p class="t" style="top:159px;right:4px;line-height:1.1">Lorem ipsum dolor sit amet, consectetur adipiscing elit, sed do eiusmod tempor incididunt ut labore et dolore magna aliqua.</p><p class="t" style="top:188px;left:10px;color:var(--gold)">Read More ⊕</p></article>
  </section>

  <section class="band contact">
    <div class="photo" role="img" aria-label="Group meditating in a sunlit forest" style="left:17px;top:27px;width:124px;height:184px;border-radius:14px 0 14px 0;background:linear-gradient(180deg,#3e5a2d 0%,#c9b277 40%,#7c6a3a 65%,#2d2a20 100%)"></div>
    <h2 class="abs heading" style="left:156px;width:236px;top:36px;text-align:center;font-size:11px">Have A Question? Contact Us Today!</h2>
    <label class="field-label" style="top:58px">Name</label><div class="field" style="top:64px">Name</div>
    <label class="field-label" style="top:80px">Email</label><div class="field" style="top:87px">Email</div>
    <label class="field-label" style="top:103px">Phone</label><div class="field" style="top:109px">Phone</div>
    <label class="field-label" style="top:125px">Subject</label><div class="field" style="top:132px">Subject</div>
    <label class="field-label" style="top:148px">Message</label><div class="field" style="top:155px;height:29px">Message</div>
    <div class="btn" style="left:156px;top:188px;width:236px;height:11px">Send Your Message</div>
  </section>

  <footer class="band footer">
    <div class="abs" style="left:19px;top:30px;font-family:'Gloock',Georgia,serif;font-size:8px">QUIETFERN MEDITATION</div>
    <p class="abs" style="left:19px;top:44px;width:122px;font-size:4.4px;line-height:1.6;text-align:justify">With us, you receive compassionate care, innovative solutions, and support at every step of your health journey.</p>
    <span class="social" style="left:23px;top:73px"></span>
    <span class="social" style="left:39px;top:73px"></span>
    <span class="social" style="left:56px;top:73px"></span>
    <span class="social" style="left:72px;top:73px"></span>
    <h4 style="left:184px;top:31px">OUR COMPANY</h4>
    <ul class="footer-links" style="top:40px">
      <li>Home</li><li>About Us</li><li>Meditation Sessions</li><li>Events &amp; Programs</li><li>Project</li><li>Resources</li><li>Volunteer With Us</li><li>Contact Us</li>
    </ul>
    <h4 style="left:287px;top:31px">GET IN TOUCH</h4>
    <p class="abs" style="left:287px;top:42px;font-size:4.4px">✉ Our Email: hello@quietfern.org</p>
    <p class="abs" style="left:287px;top:52px;font-size:4.4px">☏ Call Us: +61 400 123 456</p>
    <p class="abs" style="left:287px;top:63px;font-size:4.4px">● Visit Us: Your address will be here</p>
    <div class="abs" role="img" aria-label="Embedded street map showing the centre location" style="left:287px;top:75px;width:113px;height:43px;background:#e8ecef;border:1px solid var(--white);border-radius:2px"></div>
    <p class="abs" style="left:0;right:0;top:136px;text-align:center;font-size:4.4px">Copyright © 2026 Quietfern Meditation | Powered By Quietfern Meditation</p>
  </footer>
</section>

</body>
</html>
```